Letterhead and Stationary for Construction Company

Brisk Current needs modern Letterhead, Envelopes and Notepad designs.

Industry/Entity Type

Construction

Colors
f78f20
34a7d8
ffffff

Requirements
Must have
• Modern looking design.

```html
<!DOCTYPE html>
<html lang="en">
<head>
<meta charset="utf-8">
<title>Brisk Current Stationery</title>
<link href="https://fonts.googleapis.com/css2?family=Nunito+Sans:wght@400;600;700&family=Lato:wght@400;700&display=swap" rel="stylesheet">
<style>
  :root {
    --orange: #ed7226;
    --blue: #1f6fc2;
    --paper: #ffffff;
    --paper-soft: #f3f3f3;
    --pattern: #ececec;
    --ink: #333333;
    --backdrop: #bcbdbf;
  }
  * { box-sizing: border-box; margin: 0; padding: 0; }
  html, body { width: 1200px; height: 1200px; overflow: hidden; }
  body { background: var(--backdrop); font-family: "Lato", sans-serif; color: var(--ink); position: relative; }
  .sheet { position: absolute; background: var(--paper); overflow: hidden; }
  .flap { position: absolute; left: 0; top: 0; width: 100%; height: 60px; background: var(--orange);
          border-radius: 0 0 8px 8px; display: flex; align-items: center; justify-content: center; }
  .flap-name { font-family: "Nunito Sans", sans-serif; font-weight: 700; font-size: 20px; color: var(--paper); letter-spacing: .3px; }
  .brand { position: absolute; font-family: "Nunito Sans", sans-serif; font-weight: 700; color: var(--orange);
           line-height: 1; display: flex; align-items: center; gap: 6px; white-space: nowrap; }
  .brand-dot { width: .9em; height: .9em; border-radius: 50%; background: var(--orange); flex: none; }
  .contact { position: absolute; font-size: 6.4px; line-height: 1.35; color: var(--ink); }
  .rule { position: absolute; width: 4px; }
  .rule.orange { background: var(--orange); }
  .rule.blue { background: var(--blue); }
  .small { font-size: 6.4px; }

  .envelope-large { left: 43px; top: 60px; width: 357px; height: 504px; }
  .letterhead-blank { left: 449px; top: 60px; width: 355px; height: 502px; }
  .notepad-cover { left: 873px; top: 120px; width: 274px; height: 374px; background: var(--pattern); }
  .envelope-flap { left: 47px; top: 630px; width: 362px; height: 181px; background: var(--paper-soft); }
  .envelope-window { left: 47px; top: 873px; width: 362px; height: 170px; }
  .letter { left: 457px; top: 642px; width: 342px; height: 484px; }
  .notebook { left: 860px; top: 651px; width: 298px; height: 420px; background: var(--pattern); }

  .window { position: absolute; left: 25px; top: 63px; width: 96px; height: 48px; border-radius: 8px;
            background: linear-gradient(120deg, #f07a30 0%, #ea6a20 55%, #f18a45 60%, #ea6a20 100%); }

  .letter-body { position: absolute; left: 108px; top: 94px; width: 204px; }
  .salutation { font-size: 7px; font-weight: 700; }
  .designation { font-size: 4.8px; margin-top: 1px; }
  .company { font-size: 6.4px; font-weight: 700; margin-top: 2px; }
  .letter-body p { font-size: 5.2px; line-height: 1.3; text-align: justify; margin-top: 14px; }
  .letter-body p:first-of-type { margin-top: 24px; }
  .letter-contacts { position: absolute; left: 36px; top: 368px; width: 96px; text-align: center; font-size: 5.6px; }
  .letter-contacts li { list-style: none; margin-bottom: 14px; }
  .letter-contacts svg { display: block; margin: 0 auto 4px; }
  .sign-block { position: absolute; left: 227px; top: 366px; width: 86px; }
  .sign-name { font-size: 7px; font-weight: 700; }
  .sign-line { margin-top: 34px; border-top: 1px solid var(--ink); }
</style>
</head>
<body>

  <section class="sheet envelope-large" aria-label="Large envelope">
    <div class="flap"><span class="flap-name">Brisk Current</span></div>
    <div class="contact" style="left:45px; top:452px;">555-014-2270<br>48 Harbor Rd. Tidewater, FL 32011<br>www.briskcurrent.com</div>
  </section>

  <section class="sheet letterhead-blank" aria-label="Letterhead">
    <div class="brand" style="left:36px; top:44px; font-size:19px;"><span class="brand-dot"></span>Brisk Current</div>
    <div class="contact" style="left:44px; top:80px;">48 Harbor Rd. Tidewater, FL 32011</div>
    <div class="rule orange" style="left:42px; top:124px; height:288px;"></div>
    <div class="rule blue" style="left:52px; top:156px; height:284px;"></div>
  </section>

  <section class="sheet notepad-cover" aria-label="Notepad cover">
    <div class="brand" style="left:0; width:100%; justify-content:center; top:194px; font-size:25px;"><span class="brand-dot"></span>Brisk Current</div>
    <div class="contact" style="left:0; width:100%; text-align:center; top:352px; font-size:7px;">www.briskcurrent.com</div>
  </section>

  <section class="sheet envelope-flap" aria-label="Envelope back">
    <div class="flap"><span class="flap-name">Brisk Current</span></div>
  </section>

  <section class="sheet envelope-window" aria-label="Window envelope">
    <div class="brand" style="left:24px; top:36px; font-size:16px;"><span class="brand-dot"></span>Brisk Current</div>
    <div class="window"></div>
    <div class="contact" style="left:23px; top:130px;">555-014-2270<br>48 Harbor Rd. Tidewater, FL 32011<br>www.briskcurrent.com</div>
    <div class="rule orange" style="left:318px; top:37px; height:112px;"></div>
    <div class="rule blue" style="left:327px; top:55px; height:110px;"></div>
  </section>

  <section class="sheet letter" aria-label="Letter">
    <div class="brand" style="left:32px; top:40px; font-size:15px;"><span class="brand-dot"></span>Brisk Current</div>
    <div class="contact" style="right:33px; top:45px;">48 Harbor Rd. Tidewater, FL 32011</div>
    <div class="rule orange" style="left:60px; top:93px; height:211px;"></div>
    <div class="rule blue" style="left:70px; top:118px; height:210px;"></div>
    <div class="letter-body">
      <div class="salutation">Dear, Mr__________</div>
      <div class="designation">Designation</div>
      <div class="company">COMPANY NAME</div>
      <p>Lorem Ipsum is simply dummy text of the printing and typesetting industry. Lorem Ipsum has been the industry's standard dummy text ever since the 1500s, when an unknown printer took a galley of type and scrambled it to make a type specimen book. It has survived not only five centuries, but also the leap into electronic typesetting, remaining essentially unchanged. It was popularised in the 1960s with the release of Lumatype sheets containing Lorem Ipsum passages, and more recently with desktop publishing software like Folio Layout including versions of Lorem Ipsum.</p>
      <p>Lorem Ipsum is simply dummy text of the printing and typesetting industry. Lorem Ipsum has been the industry's standard dummy text ever since the 1500s, when an unknown printer took a galley of type and scrambled it to make a type specimen book. It has survived not only five centuries, but also the leap into electronic typesetting, remaining essentially unchanged. It was popularised in the 1960s with the release of Lumatype sheets containing Lorem Ipsum passages, and more recently with desktop publishing software like Folio Layout including versions of Lorem Ipsum.</p>
      <p>Lorem Ipsum is simply dummy text of the printing and typesetting industry. Lorem Ipsum has been the industry's standard dummy text ever since the 1500s, when an unknown printer took a galley of type and scrambled it to make a type specimen book. It has survived not only five centuries, but also the leap into electronic typesetting, remaining essentially unchanged. It was popularised in the 1960s with the release of Lumatype sheets containing Lorem Ipsum passages, and more recently with desktop publishing software like Folio Layout including versions of Lorem Ipsum.</p>
    </div>
    <ul class="letter-contacts">
      <li><svg width="7" height="7" viewBox="0 0 10 10"><path d="M2 1 L4 3 L3 4.5 Q4.5 6 5.5 7 L7 6 L9 8 L7.5 9.5 Q1 7 0.5 2.5 Z" fill="var(--orange)"/></svg>555-014-2270</li>
      <li><svg width="8" height="6" viewBox="0 0 10 7"><rect x="0" y="0" width="10" height="7" fill="var(--orange)"/><path d="M0 0 L5 4 L10 0" stroke="#fff" stroke-width="1" fill="none"/></svg>info@briskcurrent.com</li>
      <li><svg width="7" height="7" viewBox="0 0 10 10"><circle cx="5" cy="5" r="4.5" fill="var(--orange)"/><path d="M0.5 5 H9.5 M5 0.5 V9.5" stroke="#fff" stroke-width=".8"/></svg>www.briskcurrent.com</li>
    </ul>
    <div class="sign-block">
      <div class="sign-name">YOUR NAME</div>
      <div class="small">Designation</div>
      <div class="sign-line"></div>
    </div>
  </section>

  <section class="sheet notebook" aria-label="Notebook cover">
    <div class="rule orange" style="left:143px; top:278px; height:84px;"></div>
    <div class="rule blue" style="left:152px; top:288px; height:84px;"></div>
    <div class="brand" style="left:168px; top:308px; font-size:15px;"><span class="brand-dot"></span>Brisk Current</div>
    <div class="contact" style="left:170px; top:338px;">555-014-2270<br>info@briskcurrent.com<br>48 Harbor Rd. Tidewater, FL 32011<br>www.briskcurrent.com</div>
  </section>

</body>
</html>
```